R&T Builders and Spaces Business Card

We need to redesign our business card. We had used white vellum wih grey logo and txt in the past. I would like to bring a little life into our cards without being over the top. I think I will be going away from the vellum and printing soft touch business cards.
I have attached what we currently have and our new logo design.

```html
<!DOCTYPE html>
<html lang="en">
<head>
<meta charset="utf-8">
<title>R&amp;T Builders and Spaces — Business Card</title>
<link rel="stylesheet" href="https://fonts.googleapis.com/css2?family=Jost:wght@400;600&display=swap">
<style>
  :root {
    --card-charcoal: #3b3b3d;
    --card-white: #ffffff;
    --page-bg: #ffffff;
    --shadow: rgba(0, 0, 0, 0.28);
  }
  html, body {
    margin: 0;
    padding: 0;
    width: 1199px;
    height: 1200px;
    overflow: hidden;
    background: var(--page-bg);
    font-family: "Jost", "Futura", sans-serif;
  }
  .card {
    position: absolute;
    left: 166px;
    width: 868px;
    height: 512px;
    background: var(--card-charcoal);
    color: var(--card-white);
    overflow: hidden;
    box-shadow: 10px 12px 14px var(--shadow);
  }
  .card--front { top: 69px; }
  .card--back  { top: 621px; }
  .card__corners {
    position: absolute;
    inset: 0;
    width: 100%;
    height: 100%;
  }
  .contact {
    position: absolute;
    left: 84px;
    top: 98px;
    margin: 0;
    font-style: normal;
    letter-spacing: 0.3px;
  }
  .contact__name {
    margin: 0;
    font-size: 30px;
    font-weight: 600;
    line-height: 1;
    letter-spacing: 0.5px;
  }
  .contact__title {
    margin: 10px 0 0;
    font-size: 16px;
    font-weight: 400;
  }
  .contact__group {
    margin: 30px 0 0;
    font-size: 19px;
    line-height: 31px;
  }
  .brand {
    position: absolute;
    top: 117px;
  }
  .brand--front { left: 510px; }
  .brand--back  { left: 295px; }
  .brand__square {
    width: 255px;
    height: 255px;
    background: var(--card-white);
  }
  .brand__name {
    margin: 10px 0 0;
    font-size: 19px;
    font-weight: 400;
    letter-spacing: 2.4px;
    white-space: nowrap;
    color: var(--card-white);
  }
</style>
</head>
<body>

  <section class="card card--front" aria-label="Business card front">
    <svg class="card__corners" viewBox="0 0 868 512" aria-hidden="true">
      <polygon points="0,0 97,0 0,97" fill="var(--card-white)"/>
      <polygon points="0,410 0,512 102,512" fill="var(--card-white)"/>
    </svg>

    <address class="contact">
      <h1 class="contact__name">DALE M. HARTWELL</h1>
      <p class="contact__title">PRINCIPAL</p>
      <p class="contact__group">DALEH@RTBUILDERS.COM<br>T 555 214 7730&nbsp;&nbsp;C 555 318 4492</p>
      <p class="contact__group">1840 W LINDEN ST, SUITE 210<br>FAIRVIEW, ARIZONA 85099</p>
      <p class="contact__group">WWW.RTBUILDERS.COM</p>
    </address>

    <div class="brand brand--front">
      <div class="brand__square"></div>
      <p class="brand__name">R&amp;T BUILDERS AND SPACES</p>
    </div>
  </section>

  <section class="card card--back" aria-label="Business card back">
    <svg class="card__corners" viewBox="0 0 868 512" aria-hidden="true">
      <polygon points="0,0 192,0 0,192" fill="var(--card-white)"/>
      <polygon points="206,0 230,0 0,230 0,206" fill="var(--card-white)"/>
      <polygon points="868,512 676,512 868,320" fill="var(--card-white)"/>
      <polygon points="662,512 638,512 868,282 868,306" fill="var(--card-white)"/>
    </svg>

    <div class="brand brand--back">
      <div class="brand__square"></div>
      <p class="brand__name">R&amp;T BUILDERS AND SPACES</p>
    </div>
  </section>

</body>
</html>
```